Banner 170x60 for Barrel Sauna Rental Banner

Attention, please do every side graphic distance 5cm . It is for attachment.
search for a graphic design in dimension 170x60cm.
we have a barrel sauna rental service and need a banner for the two sides.
please look photos.
big text is: (I CAN RENT ME!!! )in english like: you can rent me
frohe-kistenwelt.de
015293417720
info@frohe-kistenwelt.de
we need an eye catcher design!!!!
Design:
maybe wood in at background.
maybe burning fire and sauna style.
Please don't use my barrell sauna pictures. It is only an example for you what we do. The barrel sauna is on build at the moment.

```html
<!DOCTYPE html>
<html lang="de">
<head>
<meta charset="utf-8">
<title>Fasssauna Vermietung – Banner</title>
<link rel="stylesheet" href="https://fonts.googleapis.com/css2?family=Montserrat:wght@700;800&family=Saira+Condensed:wght@700&display=swap">
<style>
  :root {
    --page: #e6e7e9;
    --banner: #000000;
    --white: #ffffff;
    --ink: #111111;
    --fire-hot: #ffb21e;
    --fire-mid: #e06a0c;
    --wood-light: #f3d8b0;
    --wood-edge: #a5623a;
    --rope: #b06a2c;
    --forest: #ecc9a2;
  }
  html, body {
    margin: 0;
    padding: 0;
    width: 1200px;
    height: 609px;
    overflow: hidden;
    background: var(--page);
  }
  .banner {
    position: absolute;
    left: 85px;
    top: 122px;
    width: 1030px;
    height: 364px;
    background: var(--banner);
    overflow: hidden;
  }
  .fire {
    position: absolute;
    left: 0;
    top: 130px;
    width: 385px;
    height: 234px;
    background:
      radial-gradient(ellipse 55% 70% at 45% 100%, var(--fire-hot) 0%, var(--fire-mid) 45%, rgba(224,106,12,0) 80%);
  }
  .forest {
    position: absolute;
    inset: 0;
    width: 1030px;
    height: 364px;
  }
  .headline {
    position: absolute;
    left: 0;
    top: 0;
    width: 1030px;
    height: 364px;
  }
  .headline text {
    font-family: "Montserrat", sans-serif;
    fill: var(--white);
    stroke: var(--banner);
    stroke-width: 3;
    paint-order: stroke;
  }
  .phone-icon {
    position: absolute;
    left: 157px;
    top: 224px;
    width: 54px;
    height: 54px;
  }
  .pill {
    position: absolute;
    top: 296px;
    height: 26px;
    background: var(--white);
    border-radius: 9px;
    display: flex;
    align-items: center;
    gap: 8px;
    padding-left: 4px;
    box-sizing: border-box;
    font-family: "Saira Condensed", sans-serif;
    font-weight: 700;
    font-size: 23px;
    letter-spacing: 0.5px;
    color: var(--ink);
    text-transform: uppercase;
  }
  .pill svg { width: 22px; height: 22px; flex: none; }
  .pill-mail { left: 100px; width: 294px; }
  .pill-web { left: 414px; width: 313px; }
  .sign {
    position: absolute;
    left: 728px;
    top: 113px;
    width: 239px;
    height: 155px;
    border-radius: 10px;
    background: linear-gradient(180deg, var(--wood-light), #e9c493);
    border: 8px solid var(--wood-edge);
    box-sizing: border-box;
  }
  .sign-name {
    position: absolute;
    left: 0;
    right: 0;
    top: 60px;
    display: flex;
    align-items: center;
    justify-content: center;
    gap: 5px;
    font-family: "Saira Condensed", sans-serif;
    font-weight: 700;
    font-size: 17px;
    color: var(--ink);
    text-transform: uppercase;
  }
  .sign-dot {
    width: 10px; height: 10px; border-radius: 50%; background: var(--ink);
  }
  .ropes { position: absolute; left: 0; top: 0; width: 1030px; height: 364px; }
</style>
</head>
<body>
  <div class="banner">
    <div class="fire" role="img" aria-label="Lodernde Flammen"></div>

    <svg class="forest" viewBox="0 0 1030 364" role="img" aria-label="Waldsilhouette mit Tannen">
      <path d="M1030 176 C1000 200 990 230 960 255 C930 285 880 320 830 335 C780 350 720 355 667 364 L1030 364 Z" fill="var(--forest)"/>
    </svg>

    <svg class="headline" viewBox="0 0 1030 364">
      <text x="73" y="144" font-size="93" font-weight="800" textLength="590" lengthAdjust="spacingAndGlyphs">SIE KÖNNEN</text>
      <text x="76" y="200" font-size="62" font-weight="800" textLength="587" lengthAdjust="spacingAndGlyphs">MICH ENGAGIEREN</text>
      <text x="215" y="272" font-size="49" font-weight="800" textLength="369" lengthAdjust="spacingAndGlyphs">015293417720</text>
    </svg>

    <svg class="phone-icon" viewBox="0 0 54 54" aria-hidden="true">
      <circle cx="27" cy="27" r="24" fill="var(--white)"/>
      <circle cx="27" cy="27" r="19" fill="none" stroke="var(--ink)" stroke-width="3"/>
      <path d="M21 15 l4 0 l2 7 l-3 3 c2 4 4 6 7 8 l3 -3 l7 2 l0 4 c-10 2 -22 -10 -20 -21 z" fill="none" stroke="var(--ink)" stroke-width="2.2" stroke-linejoin="round"/>
    </svg>

    <div class="pill pill-mail">
      <svg viewBox="0 0 22 22" aria-hidden="true">
        <circle cx="11" cy="11" r="10" fill="none" stroke="var(--ink)" stroke-width="1.6"/>
        <rect x="5.5" y="7.5" width="11" height="7.5" fill="var(--ink)"/>
        <path d="M5.5 7.5 L11 12 L16.5 7.5" fill="none" stroke="var(--white)" stroke-width="1"/>
      </svg>
      <span>info@frohe-kistenwelt.de</span>
    </div>

    <div class="pill pill-web">
      <svg viewBox="0 0 22 22" aria-hidden="true">
        <circle cx="11" cy="11" r="10" fill="none" stroke="var(--ink)" stroke-width="1.6"/>
        <circle cx="11" cy="11" r="6.5" fill="none" stroke="var(--ink)" stroke-width="1.1"/>
        <ellipse cx="11" cy="11" rx="3" ry="6.5" fill="none" stroke="var(--ink)" stroke-width="1.1"/>
        <path d="M4.5 11 H17.5 M6 7.5 H16 M6 14.5 H16" stroke="var(--ink)" stroke-width="1"/>
      </svg>
      <span>frohe-kistenwelt.de</span>
    </div>

    <svg class="ropes" viewBox="0 0 1030 364" aria-hidden="true">
      <line x1="765" y1="0" x2="767" y2="118" stroke="var(--rope)" stroke-width="5"/>
      <line x1="930" y1="0" x2="932" y2="118" stroke="var(--rope)" stroke-width="5"/>
    </svg>

    <div class="sign" role="img" aria-label="Hängendes Holzschild">
      <div class="sign-name"><span class="sign-dot"></span><span>frohe-kistenwelt.de</span></div>
    </div>
  </div>
</body>
</html>
```